v eLiquid Label

We are an electronic cigarette eLiquid manufacturer with an outdated label design which needs to be updated and become more modern. All information listed on the label cannot be changed or removed.

There are 4 colour coding on the labels that cannot change.
0mg is white
12mg is yellow
18mg is blue
24mg is red

We prefer a blue type background however are not committed to it with the proper design however if a new colour is chosen it must compliment the colour band for each colour coding

The "dots" on the front of the bottle need to be larger.

The "V" on the front needs to be in this font however we can accept slight changes to it for effect.

Issues we are facing:
The 0mg and the 18mg look too close in colour and need to be completely different in colouring.

The background colouring is too dark and you cannot see the 50/50 in the watermark.

Reason: We have not received a design which is suitable to our needs. We have see a few close ones however not exact. Thanks

Reason: I was forced to go out of country for a family emergency and to be fair I am extending the deadline

```html
<!DOCTYPE html>
<html lang="en">
<head>
<meta charset="utf-8">
<title>ORVO E-Liquid Label Set</title>
<link rel="stylesheet" href="https://fonts.googleapis.com/css2?family=Saira+Condensed:wght@600;700&display=swap">
<style>
  :root {
    --page: #ffffff;
    --label-body: #4a4a4a;
    --panel-blue: #3b7dd8;
    --panel-mark: rgba(255, 255, 255, 0.09);
    --ink-light: #ececec;
    --band-zero: #e8e8e8;
    --band-twelve: #fff200;
    --band-eighteen: #003a8c;
    --band-twentyfour: #ee0000;
    --ink-dark: #111111;
    --ink-white: #ffffff;
  }
  * { box-sizing: border-box; margin: 0; padding: 0; }
  html, body { width: 1200px; height: 720px; overflow: hidden; background: var(--page); }
  .sheet { position: relative; width: 1200px; height: 720px; }

  .label {
    position: absolute;
    width: 548px;
    height: 215px;
    background: var(--label-body);
    outline: 1px solid #9a9a9a;
  }
  .label--zero { left: 31px; top: 104px; }
  .label--twelve { left: 621px; top: 104px; }
  .label--eighteen { left: 31px; top: 399px; }
  .label--twentyfour { left: 621px; top: 399px; }

  .band {
    position: absolute;
    left: 0; right: 0;
    height: 16px;
    display: flex;
    justify-content: space-around;
    align-items: center;
    font: 700 12.5px/1 Arial, Helvetica, sans-serif;
    white-space: nowrap;
  }
  .band--top { top: 0; }
  .band--bottom { bottom: 0; }
  .band--bottom span { word-spacing: 4px; }

  .label--zero .band { background: var(--band-zero); color: var(--ink-dark); font-size: 13px; }
  .label--twelve .band { background: var(--band-twelve); color: var(--ink-dark); }
  .label--eighteen .band { background: var(--band-eighteen); color: var(--ink-white); }
  .label--twentyfour .band { background: var(--band-twentyfour); color: var(--ink-white); }

  .front {
    position: absolute;
    left: 188px;
    top: 16px;
    width: 172px;
    height: 183px;
    background: var(--panel-blue);
    overflow: hidden;
    font-family: "Saira Condensed", "Arial Narrow", sans-serif;
    color: var(--ink-light);
  }
  .ratio-mark {
    position: absolute;
    left: 8px;
    font-weight: 700;
    font-size: 50px;
    line-height: 1;
    letter-spacing: 1px;
    color: var(--panel-mark);
  }
  .ratio-mark--1 { top: 4px; }
  .ratio-mark--2 { top: 64px; }
  .ratio-mark--3 { top: 124px; }

  .brand {
    position: absolute;
    left: 0; right: 0;
    top: 30px;
    text-align: center;
    font-weight: 700;
    font-size: 52px;
    line-height: 1;
    letter-spacing: 2px;
    color: var(--ink-light);
  }
  .volume {
    position: absolute;
    right: 14px;
    top: 104px;
    font-weight: 600;
    font-size: 12px;
    line-height: 1;
  }
  .product-type {
    position: absolute;
    right: 13px;
    top: 118px;
    font-weight: 700;
    font-size: 18px;
    line-height: 1;
  }
  .flavour {
    position: absolute;
    left: 0; right: 0;
    top: 152px;
    text-align: center;
    font-weight: 700;
    font-size: 26px;
    line-height: 1;
    letter-spacing: 0.5px;
  }
  .strength-dot {
    position: absolute;
    left: 15px;
    top: 100px;
    width: 38px;
    height: 38px;
    border-radius: 50%;
    display: flex;
    align-items: center;
    justify-content: center;
    font-weight: 700;
    font-size: 24px;
    line-height: 1;
  }
  .label--twelve .strength-dot { background: var(--band-twelve); color: var(--label-body); }
  .label--eighteen .strength-dot { background: var(--band-eighteen); color: var(--ink-white); }
  .label--twentyfour .strength-dot { background: var(--band-twentyfour); color: var(--ink-white); }
</style>
</head>
<body>
<main class="sheet">

  <section class="label label--zero">
    <div class="band band--top"><span>NICOTINE FREE</span><span>NICOTINE FREE</span><span>NICOTINE FREE</span><span>NICOTINE FREE</span></div>
    <div class="front">
      <span class="ratio-mark ratio-mark--1">50/50</span>
      <span class="ratio-mark ratio-mark--2">50/50</span>
      <span class="ratio-mark ratio-mark--3">50/50</span>
      <span class="brand">ORVO</span>
      <span class="volume">30ml</span>
      <span class="product-type">E-LIQUID</span>
      <span class="flavour">SWEET TOBACCO</span>
    </div>
    <div class="band band--bottom"><span>ZERO NICOTINE</span><span>ZERO NICOTINE</span><span>ZERO NICOTINE</span><span>ZERO NICOTINE</span></div>
  </section>

  <section class="label label--twelve">
    <div class="band band--top"><span>12 mg/ml</span><span>12 mg/ml</span><span>12 mg/ml</span><span>12 mg/ml</span><span>12 mg/ml</span><span>12 mg/ml</span><span>12 mg/ml</span><span>12 mg/ml</span></div>
    <div class="front">
      <span class="ratio-mark ratio-mark--1">50/50</span>
      <span class="ratio-mark ratio-mark--2">50/50</span>
      <span class="ratio-mark ratio-mark--3">50/50</span>
      <span class="brand">ORVO</span>
      <span class="strength-dot">12</span>
      <span class="volume">30ml</span>
      <span class="product-type">E-LIQUID</span>
      <span class="flavour">SWEET TOBACCO</span>
    </div>
    <div class="band band--bottom"><span>DANGER POISON</span><span>DANGER POIZONE</span><span>DANGER POIZONE</span><span>DANGER POIZONE</span></div>
  </section>

  <section class="label label--eighteen">
    <div class="band band--top"><span>18 mg/ml</span><span>18 mg/ml</span><span>18 mg/ml</span><span>18 mg/ml</span><span>18 mg/ml</span><span>18 mg/ml</span><span>18 mg/ml</span><span>18 mg/ml</span></div>
    <div class="front">
      <span class="ratio-mark ratio-mark--1">50/50</span>
      <span class="ratio-mark ratio-mark--2">50/50</span>
      <span class="ratio-mark ratio-mark--3">50/50</span>
      <span class="brand">ORVO</span>
      <span class="strength-dot">18</span>
      <span class="volume">30ml</span>
      <span class="product-type">E-LIQUID</span>
      <span class="flavour">SWEET TOBACCO</span>
    </div>
    <div class="band band--bottom"><span>DANGER POISON</span><span>DANGER POIZONE</span><span>DANGER POIZONE</span><span>DANGER POIZONE</span></div>
  </section>

  <section class="label label--twentyfour">
    <div class="band band--top"><span>24 mg/ml</span><span>24 mg/ml</span><span>24 mg/ml</span><span>24 mg/ml</span><span>24 mg/ml</span><span>24 mg/ml</span><span>24 mg/ml</span><span>24 mg/ml</span></div>
    <div class="front">
      <span class="ratio-mark ratio-mark--1">50/50</span>
      <span class="ratio-mark ratio-mark--2">50/50</span>
      <span class="ratio-mark ratio-mark--3">50/50</span>
      <span class="brand">ORVO</span>
      <span class="strength-dot">24</span>
      <span class="volume">30ml</span>
      <span class="product-type">E-LIQUID</span>
      <span class="flavour">SWEET TOBACCO</span>
    </div>
    <div class="band band--bottom"><span>DANGER POISON</span><span>DANGER POIZONE</span><span>DANGER POIZONE</span><span>DANGER POIZONE</span></div>
  </section>

</main>
</body>
</html>
```